Based on your KWP party invitation. Could you please change to characters to be Afro Carribbean characters?

• Logo Attached and wording below.

Northvale Fairway Society 20th Anniversary
Dinner and Dance
Saturday 30th November 2013
Pellow and Greaves Banqueting Suite
Sundial Lodge London Marwick
Tealby Street
London
QZ7 4XJ
From :7PM to 2AM
Dress Code: Black Tie and Ball Gowns
Dinner Served: 8.PM SHARP
DJ: "Dell" form Manhattan
Live Jazz Band
Magicians
Mystery Guest Speaker
Overnight Accommodation available
Nearest Tube: Hadley Crescent (Marlow Line)
Parking: Facilities available in hotel and adjacent (charges apply)
TICKETS £65. 00
For more information or to reserve tickets, please visit: www.nvfs-example.co.uk

```html
<!DOCTYPE html>
<html lang="en">
<head>
<meta charset="utf-8">
<title>Northvale Fairway Society 20th Anniversary Dinner &amp; Dance</title>
<link rel="stylesheet" href="https://fonts.googleapis.com/css2?family=Cinzel:wght@400;700&family=Pinyon+Script&display=swap">
<style>
  :root {
    --backdrop: #0b0c0e;
    --gold-deep: #d39532;
    --gold-mid: #e9c457;
    --gold-light: #f6e68a;
    --rim: #f8ea8c;
    --curtain-dark: #4e0505;
    --curtain-mid: #9e1512;
    --script-red: #a81d1a;
    --date-gold: #e6b55a;
    --ink-white: #fbf6ea;
    --crest-red: #9c1820;
  }
  * { margin: 0; padding: 0; box-sizing: border-box; }
  html, body { width: 1200px; height: 1000px; overflow: hidden; background: var(--backdrop); }
  .canvas { position: relative; width: 1200px; height: 1000px; background: var(--backdrop); }
  .invitation { position: absolute; left: 334px; top: 44px; width: 532px; height: 910px; overflow: hidden; }
  .invitation-art { position: absolute; inset: 0; }
  .club-mark {
    position: absolute; top: 14px; left: 0; width: 100%;
    display: flex; flex-direction: column; align-items: center; gap: 4px;
    font-family: 'Cinzel', serif; font-weight: 700; font-size: 13px; color: var(--crest-red); letter-spacing: 1px;
  }
  .club-mark-dot { width: 34px; height: 34px; border-radius: 50%; background: var(--crest-red); }
  .event-title {
    position: absolute; top: 91px; left: 0; width: 100%; text-align: center;
    font-family: 'Cinzel', serif; font-size: 21px; line-height: 26px; color: var(--ink-white); letter-spacing: 0.5px;
  }
  .event-script { font-family: 'Pinyon Script', cursive; color: var(--script-red); position: absolute; line-height: 1; }
  .event-script.dinner { left: 72px; top: 150px; font-size: 66px; }
  .event-script.amp { left: 263px; top: 196px; font-size: 34px; }
  .event-script.dance { left: 304px; top: 206px; font-size: 66px; }
  .event-when {
    position: absolute; left: 20px; top: 719px;
    font-family: 'Cinzel', serif; font-size: 15px; line-height: 19px; color: var(--date-gold);
  }
  .event-details {
    position: absolute; left: 20px; top: 764px; list-style: none;
    font-family: 'Cinzel', serif; font-weight: 700; font-size: 10.5px; line-height: 12.9px; color: var(--ink-white);
  }
  .ticket-price {
    position: absolute; left: 370px; top: 825px;
    font-family: 'Cinzel', serif; font-size: 15px; color: var(--ink-white); letter-spacing: 0.5px;
  }
  .ticket-note {
    position: absolute; left: 352px; top: 862px; width: 184px; text-align: center;
    font-family: 'Cinzel', serif; font-size: 6.5px; line-height: 8px; color: var(--ink-white);
  }
  .ticket-web {
    position: absolute; left: 340px; top: 880px; width: 188px; text-align: center;
    font-family: 'Cinzel', serif; font-size: 12px; color: var(--ink-white); letter-spacing: 0.3px;
  }
</style>
</head>
<body>
<div class="canvas">
  <section class="invitation">
    <svg class="invitation-art" width="532" height="910" viewBox="0 0 532 910">
      <defs>
        <radialGradient id="goldGlow" cx="0.55" cy="0.42" r="0.75">
          <stop offset="0" stop-color="#f7ea8e"/>
          <stop offset="0.45" stop-color="#ecc95a"/>
          <stop offset="1" stop-color="#d39532"/>
        </radialGradient>
        <linearGradient id="curtainFill" x1="0" y1="0" x2="0" y2="1">
          <stop offset="0" stop-color="#7d0c0b"/>
          <stop offset="0.5" stop-color="#9e1512"/>
          <stop offset="1" stop-color="#4e0505"/>
        </linearGradient>
        <linearGradient id="dancerFill" x1="0" y1="0" x2="1" y2="1">
          <stop offset="0" stop-color="#2a1a22"/>
          <stop offset="0.55" stop-color="#6a2a8a"/>
          <stop offset="1" stop-color="#b06ac8" stop-opacity="0.8"/>
        </linearGradient>
      </defs>
      <rect class="curtain" width="532" height="910" fill="url(#curtainFill)" role="img" aria-label="Red stage curtain"/>
      <path class="gold-sweep" d="M0,0 H532 V656 C480,690 400,724 300,724 C160,724 40,620 0,436 Z" fill="url(#goldGlow)"/>
      <path class="gold-rim" d="M0,436 C40,620 160,724 300,724 C400,724 480,690 532,656" fill="none" stroke="var(--rim)" stroke-width="4"/>
      <ellipse class="ballroom-sketch" cx="270" cy="340" rx="235" ry="90" fill="#c9a04a" opacity="0.25" role="img" aria-label="Faint pencil sketch of a ballroom archway"/>
      <ellipse class="dancers" cx="300" cy="500" rx="140" ry="150" fill="url(#dancerFill)" opacity="0.85" role="img" aria-label="Ballroom dancing couple, man in black tuxedo and woman in purple gown"/>
    </svg>

    <div class="club-mark"><span class="club-mark-dot"></span><span>NVFS</span></div>

    <h1 class="event-title">NORTHVALE FAIRWAY<br>SOCIETY 20TH ANNIVERSARY</h1>
    <span class="event-script dinner">Dinner</span>
    <span class="event-script amp">&amp;</span>
    <span class="event-script dance">Dance</span>

    <p class="event-when">Saturday 30th November 2013<br>From :7PM to 2AM</p>
    <ul class="event-details">
      <li>DRESS CODE: BLACK TIE AND BALL GOWNS</li>
      <li>DINNER SERVED: 8.PM SHARP</li>
      <li>DJ: "DELL" FORM MANHATTAN</li>
      <li>LIVE JAZZ BAND</li>
      <li>MAGICIANS</li>
      <li>MYSTERY GUEST SPEAKER</li>
      <li>OVERNIGHT ACCOMMODATION AVAILABLE</li>
      <li>NEAREST TUBE: HADLEY CRESCENT (MARLOW LINE)</li>
      <li>PARKING: FACILITIES AVAILABLE IN HOTEL</li>
      <li>AND ADJACENT (CHARGES APPLY)</li>
    </ul>

    <p class="ticket-price">TICKETS £65. 00</p>
    <p class="ticket-note">FOR MORE INFORMATION OR TO<br>RESERVE TICKETS, PLEASE VISIT:</p>
    <p class="ticket-web">WWW.NVFS-EXAMPLE.CO.UK</p>
  </section>
</div>
</body>
</html>
```